Business cards for financial advisor-insurance agent firm

Our company, Harlow Pemberton Insurance & Investments, is an insurance (health, life, home, auto, etc) and investment brokerage offering a suite of options to meet client needs. We need business cards that are professional and embody strength, security and sophistication.

Also running a letterhead project at
http://jobs.briefmarlo.com/job.aspx?id=519087

Target Market(s)

Upper middle class and wealthy

Industry/Entity Type

Investment

Requirements
Nice to have
• Looking for either white, navy blue, or gray cards

```html
<!DOCTYPE html>
<html lang="en">
<head>
<meta charset="utf-8">
<title>Harlow Pemberton Insurance &amp; Investments — Business Cards</title>
<link rel="stylesheet" href="https://fonts.googleapis.com/css2?family=Cinzel:wght@400&family=Marcellus&family=Open+Sans:wght@400;700&display=swap">
<style>
  :root {
    --backdrop: #e8e5e0;
    --white-card: #ffffff;
    --navy-card: #3b4368;
    --gray-card: #8b8c8e;
    --ink-navy: #242a4b;
    --ink-slate: #5d6e79;
    --ink-pale: #a9b8c2;
    --ink-light: #e2e4e6;
    --frame-light: #d9dadb;
    --card-shadow: 0 6px 14px rgba(0, 0, 0, 0.18);
  }

  * { box-sizing: border-box; margin: 0; padding: 0; }

  html, body {
    width: 1200px;
    height: 750px;
    overflow: hidden;
    background: var(--backdrop);
  }

  .canvas {
    position: relative;
    width: 1200px;
    height: 750px;
  }

  .card {
    position: absolute;
    width: 188px;
    height: 310px;
    box-shadow: var(--card-shadow);
    text-align: center;
  }

  .card--white { background: var(--white-card); }
  .card--navy  { background: var(--navy-card); }
  .card--gray  { background: var(--gray-card); }

  /* placement */
  .pos-white-front { left: 36px;  top: 42px; }
  .pos-white-back  { left: 250px; top: 158px; }
  .pos-navy-front  { left: 682px; top: 26px; }
  .pos-navy-back   { left: 937px; top: 78px; }
  .pos-gray-front  { left: 462px; top: 380px; }
  .pos-gray-back   { left: 672px; top: 406px; }

  /* front side */
  .brand-square {
    position: absolute;
    left: 62px;
    top: 14px;
    width: 64px;
    height: 64px;
    border: 3px solid var(--ink-navy);
  }
  .card--navy .brand-square { border-color: var(--ink-pale); }

  .die-window {
    position: absolute;
    left: 34px;
    top: 96px;
    width: 120px;
    height: 118px;
    background: var(--backdrop);
    box-shadow: inset 3px 4px 6px rgba(0, 0, 0, 0.35);
  }

  .firm-name {
    position: absolute;
    left: 0;
    right: 0;
    top: 238px;
    font-family: "Cinzel", serif;
    font-weight: 400;
    color: var(--ink-navy);
    line-height: 1.15;
  }
  .firm-name__main { display: block; font-size: 15px; letter-spacing: 0.2px; }
  .firm-name__sub  { display: block; font-size: 7.4px; letter-spacing: 0.3px; }
  .card--navy .firm-name { color: var(--ink-pale); }

  /* back side */
  .agent-name {
    position: absolute;
    left: 0;
    right: 0;
    top: 26px;
    font-family: "Marcellus", serif;
    font-size: 21px;
    line-height: 1;
    color: var(--ink-navy);
    text-transform: uppercase;
  }
  .agent-title {
    position: absolute;
    left: 0;
    right: 0;
    top: 52px;
    font-family: "Marcellus", serif;
    font-size: 10px;
    letter-spacing: 0.4px;
    color: var(--ink-slate);
    text-transform: uppercase;
  }
  .card--navy .agent-name,
  .card--navy .agent-title { color: var(--ink-pale); }
  .card--gray .agent-title { color: var(--ink-light); }

  .photo-frame {
    position: absolute;
    left: 24px;
    top: 80px;
    width: 140px;
    height: 136px;
    border: 7px solid var(--ink-slate);
  }
  .card--navy .photo-frame { border-color: #6f818c; }
  .card--gray .photo-frame { border-color: var(--frame-light); }

  .photo-frame .die-window {
    left: 9px;
    top: 9px;
    width: 108px;
    height: 104px;
  }

  .contact {
    position: absolute;
    left: 0;
    right: 0;
    top: 232px;
    font-family: "Open Sans", sans-serif;
    font-size: 8.6px;
    line-height: 1;
    color: var(--ink-navy);
    list-style: none;
  }
  .contact li { margin-bottom: 11px; }
  .contact b { font-weight: 700; }
  .card--navy .contact { color: var(--ink-light); }
  .card--gray .contact b { color: var(--ink-navy); }
</style>
</head>
<body>
<main class="canvas">

  <!-- White set -->
  <section class="card card--white pos-white-front" aria-label="White card, front">
    <div class="brand-square"></div>
    <div class="die-window"></div>
    <h2 class="firm-name">
      <span class="firm-name__main">Harlow Pemberton</span>
      <span class="firm-name__sub">Insurance &amp; Investments</span>
    </h2>
  </section>

  <section class="card card--white pos-white-back" aria-label="White card, back">
    <h1 class="agent-name">Daniel Whitford</h1>
    <p class="agent-title">Insurance Agent</p>
    <div class="photo-frame"><div class="die-window"></div></div>
    <ul class="contact">
      <li><b>Tel:</b> 555-0142</li>
      <li><b>E-mail:</b> daniel@harlowpemberton.com</li>
      <li><b>www.harlowpemberton.com</b></li>
    </ul>
  </section>

  <!-- Navy set -->
  <section class="card card--navy pos-navy-front" aria-label="Navy card, front">
    <div class="brand-square"></div>
    <div class="die-window"></div>
    <h2 class="firm-name">
      <span class="firm-name__main">Harlow Pemberton</span>
      <span class="firm-name__sub">Insurance &amp; Investments</span>
    </h2>
  </section>

  <section class="card card--navy pos-navy-back" aria-label="Navy card, back">
    <h1 class="agent-name">Daniel Whitford</h1>
    <p class="agent-title">Insurance Agent</p>
    <div class="photo-frame"><div class="die-window"></div></div>
    <ul class="contact">
      <li><b>Tel:</b> 555-0142</li>
      <li><b>E-mail:</b> daniel@harlowpemberton.com</li>
      <li><b>www.harlowpemberton.com</b></li>
    </ul>
  </section>

  <!-- Gray set -->
  <section class="card card--gray pos-gray-front" aria-label="Gray card, front">
    <div class="brand-square"></div>
    <div class="die-window"></div>
    <h2 class="firm-name">
      <span class="firm-name__main">Harlow Pemberton</span>
      <span class="firm-name__sub">Insurance &amp; Investments</span>
    </h2>
  </section>

  <section class="card card--gray pos-gray-back" aria-label="Gray card, back">
    <h1 class="agent-name">Daniel Whitford</h1>
    <p class="agent-title">Insurance Agent</p>
    <div class="photo-frame"><div class="die-window"></div></div>
    <ul class="contact">
      <li><b>Tel:</b> 555-0142</li>
      <li><b>E-mail:</b> daniel@harlowpemberton.com</li>
      <li><b>www.harlowpemberton.com</b></li>
    </ul>
  </section>

</main>
</body>
</html>
```